I want a double sided flyer possibly with a picture of a lawn or grass.
Company name, phone number, email, and logo
Halvorsen Turf Management, (404)726-1853,Halvorsen_Turf@brevimail.com
Company services
Fertilization and weed control,Lawn and Landscape maintenance, mowing, pruning, aeration, landscape and Christmas lights,

```html
<!DOCTYPE html>
<html lang="en">
<head>
<meta charset="utf-8">
<title>Halvorsen Turf Management – Flyer</title>
<link rel="stylesheet" href="https://fonts.googleapis.com/css2?family=Fjalla+One&family=Arimo:wght@400;700&display=swap">
<style>
  :root {
    --page: #ffffff;
    --lime: #b4ef3c;
    --leaf: #8fdc34;
    --grass: #4a9e18;
    --forest: #1f5a0c;
    --deep: #123a07;
    --peach: #f3d3b4;
    --ink: #0f1a08;
    --white: #ffffff;
    --earth-top: #9b8c84;
    --earth-bottom: #3e2f26;
  }
  * { box-sizing: border-box; margin: 0; padding: 0; }
  html, body { width: 1200px; height: 848px; overflow: hidden; background: var(--page); }
  .canvas { position: relative; width: 1200px; height: 848px; }

  .flyer {
    position: absolute; top: 48px; width: 530px; height: 750px; overflow: hidden;
    box-shadow: 6px 6px 8px rgba(0,0,0,.35);
  }

  /* Front side */
  .flyer--front {
    left: 52px;
    background: linear-gradient(180deg, var(--leaf) 0%, var(--lime) 28%, var(--grass) 46%, var(--forest) 66%, var(--deep) 100%);
  }
  .front-name {
    position: absolute; left: 0; right: 0; top: 262px; text-align: center;
    font-family: "Arimo", Arial, sans-serif; font-weight: 700; font-size: 40px;
    line-height: 46px; color: var(--peach);
  }
  .front-name__mark {
    display: block; width: 76px; height: 76px; margin: 0 auto 30px;
    border-radius: 50%; background: var(--peach);
  }
  .contact {
    position: absolute; left: 0; right: 0; top: 510px; text-align: center;
    font-family: "Arimo", Arial, sans-serif; font-weight: 700; font-size: 18px;
    color: var(--peach); line-height: 25px;
  }
  .contact__line { display: flex; justify-content: center; align-items: center; gap: 5px; }
  .contact__icon {
    width: 17px; height: 17px; border-radius: 50%; background: var(--peach);
    color: var(--deep); font-size: 11px; line-height: 17px; text-align: center;
  }

  /* Back side */
  .flyer--back {
    left: 610px;
    background: linear-gradient(180deg, var(--earth-top) 0%, #6c5a50 40%, var(--earth-bottom) 70%);
  }
  .grass-photo {
    position: absolute; left: 0; right: 0; bottom: 0; height: 320px;
    background: linear-gradient(180deg, rgba(90,170,30,0) 0%, #4fb51c 30%, #7de02e 55%, #3f9a14 100%);
  }
  .service-card {
    position: absolute; left: 37px; top: 34px; width: 457px; height: 480px;
    border-radius: 22px;
    background: linear-gradient(180deg, rgba(170,230,140,.92) 0%, rgba(60,170,40,.85) 45%, rgba(70,180,40,.55) 80%, rgba(90,200,40,0) 100%);
  }
  .headline {
    position: absolute; left: 0; right: 0; top: 38px; text-align: center;
    font-family: "Fjalla One", "Arial Narrow", sans-serif; font-weight: 400; font-size: 25px;
    line-height: 32px; color: var(--ink);
  }
  .services-intro {
    position: absolute; left: 0; right: 0; top: 176px; text-align: center;
    font-family: "Fjalla One", "Arial Narrow", sans-serif; font-size: 15px; color: var(--ink);
  }
  .services { position: absolute; left: 0; right: 0; top: 210px; list-style: none; }
  .services__item {
    position: relative; height: 33px; padding-left: 98px;
    font-family: "Fjalla One", "Arial Narrow", sans-serif; font-size: 18px;
    line-height: 33px; color: var(--ink);
  }
  .services__item::after {
    content: ""; position: absolute; left: 10px; right: 100px; bottom: 0; height: 3px;
    background: linear-gradient(90deg, rgba(255,255,255,0), rgba(200,255,170,.7) 30%, rgba(200,255,170,.7) 70%, rgba(255,255,255,0));
  }
  .services__item::before {
    content: ""; position: absolute; left: 86px; top: 13px; width: 7px; height: 7px; background: var(--ink);
  }
  .back-name {
    position: absolute; left: 0; right: 0; top: 600px; text-align: center;
    font-family: "Fjalla One", "Arial Narrow", sans-serif; font-size: 34px;
    line-height: 1.15; color: var(--white);
  }
</style>
</head>
<body>
<main class="canvas">
  <section class="flyer flyer--front">
    <div class="front-name"><span class="front-name__mark"></span>Halvorsen Turf<br>Management</div>
    <div class="contact">
      <p class="contact__line"><span class="contact__icon">p</span>(404)726-1853</p>
      <p class="contact__line"><span class="contact__icon">e</span>Halvorsen_Turf@brevimail.com</p>
    </div>
  </section>

  <section class="flyer flyer--back">
    <div class="grass-photo" role="img" aria-label="Close-up photo of fresh green grass and clover"></div>
    <div class="service-card">
      <h1 class="headline">Halvorsen Turf Management can take<br>care of your lawns and<br>your landscape to make everything<br>healthy and beautiful.</h1>
      <p class="services-intro">Halvorsen Turf Management company services;</p>
      <ul class="services">
        <li class="services__item">Fertilization and weed control</li>
        <li class="services__item">Lawn and Landscape maintenance</li>
        <li class="services__item">Mowing</li>
        <li class="services__item">Pruning</li>
        <li class="services__item">Aeration</li>
        <li class="services__item">Landscape</li>
        <li class="services__item">Christmas lights</li>
      </ul>
    </div>
    <div class="back-name">Halvorsen Turf<br>Management</div>
  </section>
</main>
</body>
</html>
```